Lake to Lake Striding Gala promotion card

The card will advertise a high quality running event that has been listed in Jogger's Ledger as one of the best in the country. My hobby business Bolvane Sprints puts on high quality events that cater to being the best. Needing to be included: half marathon, 10K/5K, September 12 is the date, voted best half marathon in Iowa, Flat and fast NQLB courses, post race party includes pizza, BBQ, beer, chocolate milk, massages, Iowa NQLB half marathon championshoips. Register at bolvanesprints.example.

Target Market(s)

Runners and walkers

Industry/Entity Type

Fitness

Font styles to use
Serif

Requirements
Must have
• Eye catching, race distances, color matching the logo, my Bolvane logo somewhere on it, QR code to use for registering needs to be incorporated

```html
<!DOCTYPE html>
<html lang="en">
<head>
<meta charset="utf-8">
<title>Lake to Lake Striding Gala – Promotion Card</title>
<link rel="stylesheet" href="https://fonts.googleapis.com/css2?family=Merriweather:wght@400;700;900&family=Roboto:wght@400;700&display=swap">
<style>
  :root {
    --page-bg: #e9ebe4;
    --forest: #0d4a22;
    --forest-deep: #062f15;
    --leaf: #3f8f2a;
    --lime: #b7d431;
    --lime-bright: #d9ec3a;
    --sun: #f2e21c;
    --white: #ffffff;
    --ink: #2a2a2a;
    --rule: #9a9a9a;
    --olive: #6f8f24;
  }
  * { box-sizing: border-box; margin: 0; padding: 0; }
  html, body { width: 900px; height: 1200px; overflow: hidden; }
  body {
    background: var(--page-bg);
    font-family: "Roboto", Arial, sans-serif;
    position: relative;
  }
  .card {
    position: absolute;
    left: 60px;
    width: 780px;
    height: 545px;
    overflow: hidden;
    box-shadow: 0 6px 18px rgba(0,0,0,.25);
  }
  .card--front { top: 40px; background: linear-gradient(135deg, var(--forest-deep), var(--forest) 55%, var(--leaf)); }
  .card--back { top: 615px; background: var(--white); }

  .swooshes { position: absolute; inset: 0; width: 100%; height: 100%; }

  .photo {
    position: absolute;
    border-radius: 50%;
    border: 5px solid var(--white);
    box-shadow: 0 3px 10px rgba(0,0,0,.35);
  }

  /* Front */
  .headline {
    position: absolute; left: 215px; top: 26px;
    color: var(--sun); font-weight: 700; font-size: 34px; letter-spacing: 1px;
  }
  .date {
    position: absolute; left: 330px; top: 70px;
    color: var(--white); font-weight: 700; font-size: 24px;
    font-family: "Merriweather", Georgia, serif;
  }
  .photo--hero { left: 218px; top: 118px; width: 190px; height: 190px;
    background: radial-gradient(circle at 50% 40%, #5fd3e6, #1a8fb3 70%, #0d5e80); }
  .photo--group { left: 108px; top: 272px; width: 145px; height: 145px;
    background: linear-gradient(160deg, #9bc2d8, #c9b89a 55%, #6f7f5a); }
  .photo--solo { left: 600px; top: 395px; width: 120px; height: 120px;
    background: linear-gradient(170deg, #a7c5d6, #b39a84 55%, #7b6a52); }

  .event-mark {
    position: absolute; left: 445px; top: 160px; width: 310px; text-align: center;
  }
  .event-name {
    font-family: "Merriweather", Georgia, serif; font-weight: 900;
    font-size: 40px; color: var(--white); line-height: 1;
    display: inline-flex; align-items: center; gap: 10px;
  }
  .event-name .dot { width: 14px; height: 14px; border-radius: 50%; background: var(--sun); }
  .distances {
    margin-top: 10px;
    font-family: "Merriweather", Georgia, serif; font-weight: 700;
    font-size: 15px; letter-spacing: 1.5px; color: var(--sun);
  }
  .accolade {
    margin-top: 10px;
    font-family: "Merriweather", Georgia, serif; font-weight: 700;
    font-size: 13px; color: var(--white); letter-spacing: .5px;
  }

  .organiser {
    position: absolute; left: 40px; top: 435px;
    font-family: "Merriweather", Georgia, serif; font-weight: 900;
    font-size: 24px; color: var(--white);
    display: flex; align-items: center; gap: 8px;
  }
  .organiser .mark { width: 14px; height: 14px; background: var(--sun); }
  .url {
    position: absolute; left: 200px; width: 380px; bottom: 22px; text-align: center;
    color: var(--sun); font-weight: 700; font-size: 19px;
  }

  /* Back */
  .back-panel {
    position: absolute; left: 0; top: 0; bottom: 0; width: 345px;
    background: linear-gradient(180deg, var(--lime) 0%, var(--olive) 55%, var(--forest) 100%);
    display: flex; flex-direction: column; align-items: center;
    padding-top: 26px; color: var(--white);
  }
  .back-panel .event-name { font-size: 32px; color: var(--forest-deep); }
  .back-panel .event-name .dot { background: var(--forest-deep); width: 11px; height: 11px; }
  .back-panel .distances { font-size: 12px; color: var(--forest-deep); margin-top: 6px; }
  .photo-stack { position: relative; width: 220px; height: 160px; margin-top: 18px; }
  .photo--finish { left: 70px; top: 0; width: 120px; height: 120px;
    background: linear-gradient(160deg, #c7c1b0, #8a9a6a 60%, #4f5e3a); }
  .photo--pack { left: 10px; top: 55px; width: 100px; height: 100px;
    background: linear-gradient(160deg, #b3c9d2, #a38a6c 60%, #5d5040); }
  .pitch {
    margin-top: 14px; width: 260px; text-align: center;
    font-family: "Merriweather", Georgia, serif; font-size: 12.5px;
    line-height: 1.55; letter-spacing: .6px; text-transform: uppercase;
  }
  .back-panel .organiser {
    position: static; margin-top: 22px; align-self: flex-start; margin-left: 30px;
    font-size: 17px; color: var(--sun);
  }
  .back-panel .organiser .mark { width: 10px; height: 10px; }
  .back-panel .url { position: static; width: auto; margin-top: 12px; font-size: 16px; color: var(--white); }

  .facts {
    position: absolute; left: 365px; top: 30px; width: 140px;
    font-family: "Merriweather", Georgia, serif; color: var(--forest);
  }
  .facts h2 { font-size: 13px; font-weight: 900; line-height: 1.3; margin-bottom: 10px; color: var(--forest-deep); }
  .facts ul { list-style: none; }
  .facts li {
    font-size: 10.5px; line-height: 1.45; margin-bottom: 9px;
    padding-left: 12px; position: relative;
  }
  .facts li::before {
    content: ""; position: absolute; left: 0; top: 5px;
    width: 6px; height: 6px; border-radius: 50%; background: var(--leaf);
  }
  .register { position: absolute; left: 365px; top: 390px; width: 140px; text-align: center; }
  .qr {
    width: 96px; height: 96px; margin: 0 auto 8px;
    border: 3px solid var(--forest-deep); background: var(--white);
    display: flex; align-items: center; justify-content: center;
  }
  .register p {
    font-family: "Merriweather", Georgia, serif; font-size: 10px; font-weight: 700;
    color: var(--forest-deep); line-height: 1.4;
  }

  .divider { position: absolute; left: 520px; top: 150px; width: 1px; height: 300px; background: var(--rule); }
  .stamp-box {
    position: absolute; right: 38px; top: 36px; width: 92px; height: 108px;
    border: 2px solid var(--rule);
  }
  .address-lines { position: absolute; left: 555px; right: 38px; top: 300px; }
  .address-lines span { display: block; height: 1px; background: var(--rule); margin-bottom: 50px; }
</style>
</head>
<body>

<section class="card card--front" aria-label="Card front">
  <svg class="swooshes" viewBox="0 0 780 545" preserveAspectRatio="none" aria-hidden="true">
    <path d="M0 150 C200 60 420 120 560 230 C660 310 720 300 780 270 L780 320 C700 360 620 340 540 280 C400 170 220 120 0 200 Z" fill="#b7d431" opacity=".85"/>
    <path d="M0 230 C180 170 360 240 470 330 C570 410 690 420 780 380 L780 410 C690 460 560 440 450 360 C340 280 180 230 0 270 Z" fill="#d9ec3a" opacity=".9"/>
    <path d="M0 330 C150 290 300 360 420 430 C520 490 660 500 780 470 L780 545 L0 545 Z" fill="#3f8f2a" opacity=".8"/>
    <path d="M0 380 C170 350 320 420 430 480 C520 525 650 530 780 505 L780 520 C650 545 520 545 420 500 C310 445 170 385 0 405 Z" fill="#d9ec3a" opacity=".75"/>
    <path d="M420 0 C520 60 640 80 780 40 L780 90 C640 130 520 100 420 0 Z" fill="#b7d431" opacity=".5"/>
  </svg>
  <p class="headline">COMING SOON...</p>
  <p class="date">12 September</p>
  <div class="photo photo--hero" role="img" aria-label="Silhouettes of runners against a bright blue sky"></div>
  <div class="photo photo--group" role="img" aria-label="Group of runners on a road race course"></div>
  <div class="photo photo--solo" role="img" aria-label="Runner on a trail beside a stone wall"></div>
  <div class="event-mark">
    <div class="event-name"><span class="dot"></span>Lake to Lake</div>
    <p class="distances">HALF MARATHON | 10K | 5K</p>
    <p class="accolade">Voted Best Half Marathon in Iowa</p>
  </div>
  <div class="organiser"><span class="mark"></span>Bolvane Sprints</div>
  <p class="url">www.bolvanesprints.example</p>
</section>

<section class="card card--back" aria-label="Card back">
  <div class="back-panel">
    <div class="event-name"><span class="dot"></span>Lake to Lake</div>
    <p class="distances">HALF MARATHON | 10K | 5K</p>
    <div class="photo-stack">
      <div class="photo photo--finish" role="img" aria-label="Runners crossing the finish area"></div>
      <div class="photo photo--pack" role="img" aria-label="Pack of runners at the start line"></div>
    </div>
    <p class="pitch">A high quality running event that has been listed in Jogger's Ledger as one of the best in the country</p>
    <div class="organiser"><span class="mark"></span>Bolvane Sprints</div>
    <p class="url">www.bolvanesprints.example</p>
  </div>

  <div class="facts">
    <h2>September 12<br>Half Marathon · 10K · 5K</h2>
    <ul>
      <li>Voted best half marathon in Iowa</li>
      <li>Flat and fast NQLB courses</li>
      <li>Iowa NQLB Half Marathon Championships</li>
      <li>Post race party: pizza, BBQ, beer, chocolate milk, massages</li>
    </ul>
  </div>

  <div class="register">
    <div class="qr" role="img" aria-label="QR code for registering at bolvanesprints.example"></div>
    <p>Scan to register<br>bolvanesprints.example</p>
  </div>

  <div class="divider"></div>
  <div class="stamp-box" aria-label="Stamp area"></div>
  <div class="address-lines" aria-label="Address lines"><span></span><span></span><span></span><span></span></div>
</section>

</body>
</html>
```